Parades of Glint stationary design

Parades of Glint (www.paradesofglint.example) is a company that operates events that display the worlds most exotic cars, motorcyles, aircraft, watercraft and luxury brands. we are cutting edge and are looking for a clean , modern stationary design. our sponsors of the events include names like Vantorro, Molvecci, Castelvandri, Kelmayr, Ravelli, Lun vorel, Quastmere and many other big names. we currently operate in florida but are looking to get into new York and California. I added the logo and two car images.car images are optional and not mandatory for the design. Just thought we would add to see what happens.

Target Market(s)

high end , clean design think KELMAYR DESGN style sharp, clean, cutting edge must appeal to the high end luxury brand corporate companies and car, motorcycle, boat, aircraft and luxury brand collectors

Industry/Entity Type

Events

Font styles to use
Sans Serif

Requirements
Must have
• our contact information
• Neil Horvath
• President
• 352-555-0174
• www.paradesofglint.example
• PO Box 4862
• Dunmore, FL 32000
• for business card my email is neil@paradesofglint.example

```html
<!DOCTYPE html>
<html lang="en">
<head>
<meta charset="utf-8">
<title>Parades of Glint – Stationery</title>
<link href="https://fonts.googleapis.com/css2?family=Questrial&family=Montserrat:wght@600&display=swap" rel="stylesheet">
<style>
  :root {
    --backdrop: #d6d6d6;
    --paper: #f3f3f3;
    --ink: #3a3a3a;
    --ink-soft: #6b6b6b;
    --brand-red: #b82025;
    --band-grey: #a19c9b;
    --folder: #2b2a2a;
    --folder-spine: #232222;
  }
  * { box-sizing: border-box; margin: 0; padding: 0; }
  html, body { width: 1200px; height: 1000px; overflow: hidden; }
  body {
    position: relative;
    background: var(--backdrop);
    font-family: "Questrial", sans-serif;
    color: var(--ink);
  }
  .piece { position: absolute; overflow: hidden; }
  .paper { background: var(--paper); }

  .footer-band {
    position: absolute; left: 0; bottom: 0; width: 100%;
    background: linear-gradient(90deg, var(--band-grey) 0%, #c9c5c4 40%, var(--brand-red) 100%);
  }

  .brand-name {
    font-family: "Questrial", sans-serif;
    color: var(--ink-soft);
    line-height: 0.95;
    letter-spacing: 0.02em;
    text-transform: uppercase;
    white-space: nowrap;
  }
  .brand-name--light { color: #ffffff; }

  /* Letterhead */
  .letterhead { left: 140px; top: 82px; width: 448px; height: 582px; }
  .letterhead .brand-name { position: absolute; left: 41px; top: 40px; font-size: 16px; }
  .letterhead-contact { position: absolute; left: 268px; top: 44px; display: flex; gap: 8px; font-size: 6px; line-height: 8.5px; }
  .contact-divider { width: 1px; background: #b5b5b5; }
  .contact-line { display: flex; align-items: center; gap: 3px; }
  .contact-line svg { width: 6px; height: 6px; flex: none; }
  .letter { position: absolute; left: 41px; top: 186px; width: 366px; font-size: 6.1px; line-height: 7.9px; color: #4a4a4a; }
  .letter-greeting { font-family: "Montserrat", sans-serif; font-weight: 600; margin-bottom: 7px; }
  .letter p { margin-bottom: 7px; text-align: justify; }
  .letter-closing { margin-top: 13px; }
  .letter-signer { font-family: "Montserrat", sans-serif; font-weight: 600; }
  .signature { position: absolute; left: 95px; top: 376px; width: 95px; height: 45px; background: linear-gradient(120deg, rgba(74,95,176,0.05), rgba(74,95,176,0.22), rgba(74,95,176,0.05)); border-radius: 20px; }
  .letterhead .footer-band { height: 26px; }

  /* Business card */
  .card-front { left: 640px; top: 82px; width: 184px; height: 105px; }
  .card-holder { position: absolute; left: 14px; top: 16px; }
  .card-holder-name { font-family: "Montserrat", sans-serif; font-weight: 600; font-size: 5.6px; color: var(--brand-red); letter-spacing: 0.04em; text-transform: uppercase; }
  .card-holder-role { font-size: 4.6px; color: var(--ink-soft); margin-top: 1px; }
  .card-front .brand-name { position: absolute; left: 100px; top: 15px; font-size: 10px; }
  .card-contact { position: absolute; left: 14px; top: 54px; font-size: 4.6px; line-height: 6px; color: var(--ink-soft); }
  .card-contact .contact-line svg { width: 4.5px; height: 4.5px; }
  .card-address { margin-top: 3px; }
  .card-front .footer-band { height: 14px; }

  .card-back { left: 875px; top: 82px; width: 185px; height: 105px; background: var(--folder); }
  .card-back .brand-name { position: absolute; left: 52px; top: 40px; font-size: 12px; }

  /* Folder */
  .folder { left: 640px; top: 238px; width: 463px; height: 602px; background: var(--folder); border-radius: 4px; }
  .folder-spine { position: absolute; left: 0; top: 0; width: 28px; height: 100%; background: var(--folder-spine); border-right: 1px solid #1a1a1a; }
  .folder .brand-name { position: absolute; left: 210px; top: 94px; font-size: 30px; }

  /* Envelope */
  .envelope { left: 87px; top: 713px; width: 501px; height: 218px; }
  .envelope .brand-name { position: absolute; left: 24px; top: 25px; font-size: 16px; }
  .envelope-address { position: absolute; left: 140px; top: 28px; font-size: 6px; line-height: 8px; color: var(--ink-soft); }
  .envelope .footer-band { height: 22px; }
</style>
</head>
<body>

<section class="piece paper letterhead" aria-label="Letterhead">
  <div class="brand-name">Parades<br>of Glint</div>
  <div class="letterhead-contact">
    <div>PO Box 4862<br>Dunmore, FL 32000</div>
    <div class="contact-divider"></div>
    <div>
      <div class="contact-line">
        <svg viewBox="0 0 10 10"><circle cx="5" cy="5" r="4.5" fill="none" stroke="#b82025"/><path d="M3.2 2.8c.4 2 1.6 3.4 3.6 4.2l.6-1-1-.6-.5.5c-.8-.4-1.4-1-1.8-1.8l.5-.5-.6-1z" fill="#b82025"/></svg>
        352-555-0174
      </div>
      <div class="contact-line">
        <svg viewBox="0 0 10 10"><circle cx="5" cy="5" r="4.5" fill="#b82025"/><circle cx="5" cy="5" r="2.6" fill="none" stroke="#fff" stroke-width=".7"/><path d="M2.4 5h5.2M5 2.4v5.2" stroke="#fff" stroke-width=".6"/></svg>
        www.paradesofglint.example
      </div>
    </div>
  </div>

  <div class="letter">
    <div class="letter-greeting">Dear sir,</div>
    <p>Communication is a very integral part of living creatures, animals and humans. Communication may be verbal or written. Written communication however is only applicable to human beings. Can you even imagine a world without communication? Verbal communication can be through telephones, webcams or in person. Written communication is through letters, emails and mobile phone messages.</p>
    <p>In today's world of great inventions and technology, letters have somehow become redundant. It is the time for text messages or chats. But they still can communicate a lot more than all other modes of communication. Organizations and various government departments still bank on letters as a strong medium of communication. There is no comparison in costs of sending letters as compared to costs of mobile phone messages though – letters are far cheaper. Letters now commonly known as "hard copy documents" are considered more relevant and important than email copies of text messages as proof or evidence of some sort.</p>
    <p>Letters speak volumes about a person or an organization that writes it. So one must take utmost care ensuring that the language used in any letter is appropriate for the occasion for which it is being written. Since a letter is also a written proof or document, if there are certain things that should not form a part of it, then that too should be carefully handled.</p>
    <p>Writing a good letter is an art. But if for some reason someone is unable to write that perfect letter, these different types of letters provide a base for you to build on. Sample letters have been given for everyone to understand what all information needs to form a part of the letter type and then it can be customized.</p>
    <div class="letter-closing">Yours Sincerely,</div>
    <div class="letter-signer">Tova Renlick</div>
  </div>
  <div class="signature" role="img" aria-label="Handwritten signature in blue ink"></div>

  <div class="footer-band" role="img" aria-label="Decorative grey and red curved footer wave"></div>
</section>

<section class="piece paper card-front" aria-label="Business card front">
  <div class="card-holder">
    <div class="card-holder-name">Neil Horvath</div>
    <div class="card-holder-role">President</div>
  </div>
  <div class="brand-name">Parades<br>of Glint</div>
  <div class="card-contact">
    <div class="contact-line">
      <svg viewBox="0 0 10 10"><circle cx="5" cy="5" r="5" fill="#b82025"/><path d="M3.2 2.8c.4 2 1.6 3.4 3.6 4.2l.6-1-1-.6-.5.5c-.8-.4-1.4-1-1.8-1.8l.5-.5-.6-1z" fill="#fff"/></svg>
      352-555-0174
    </div>
    <div class="contact-line">
      <svg viewBox="0 0 10 10"><circle cx="5" cy="5" r="5" fill="#b82025"/><rect x="2.6" y="3.3" width="4.8" height="3.4" fill="none" stroke="#fff" stroke-width=".6"/><path d="M2.6 3.3L5 5.2l2.4-1.9" fill="none" stroke="#fff" stroke-width=".6"/></svg>
      neil@paradesofglint.example
    </div>
    <div class="contact-line">
      <svg viewBox="0 0 10 10"><circle cx="5" cy="5" r="5" fill="#b82025"/><circle cx="5" cy="5" r="2.6" fill="none" stroke="#fff" stroke-width=".7"/><path d="M2.4 5h5.2M5 2.4v5.2" stroke="#fff" stroke-width=".6"/></svg>
      www.paradesofglint.example
    </div>
    <div class="card-address">PO Box 4862<br>Dunmore, FL 32000</div>
  </div>
  <div class="footer-band" role="img" aria-label="Decorative grey and red curved footer wave"></div>
</section>

<section class="piece card-back" aria-label="Business card back">
  <div class="brand-name brand-name--light">Parades<br>of Glint</div>
</section>

<section class="piece folder" aria-label="Presentation folder">
  <div class="folder-spine"></div>
  <div class="brand-name brand-name--light">Parades<br>of Glint</div>
</section>

<section class="piece paper envelope" aria-label="Envelope">
  <div class="brand-name">Parades<br>of Glint</div>
  <div class="envelope-address">PO Box 4862<br>Dunmore, FL 32000</div>
  <div class="footer-band" role="img" aria-label="Decorative grey and red curved footer wave"></div>
</section>

</body>
</html>
```